Modern and sophisticated web design for architect/designer

Vantor Loom is a Building Design & Drafting studio based in Nedlands Western Australia, providing a high quality and complete client service from concept design through Council planning approvals and building licenses to construction drawings for kitchens and bathrooms, extensions, additions, renovations and new homes.

Vantor Loom is looking for a new qwerty design that *is different from a normal* 2/3 column website. The website design must be very arty, clean and catchy. This design needs to be very different and must not look like a downloadable template.

The design must be able to display a lot of photos for the different projects.

The design must comply with W3C standards (i.e. use of fonts) and must be delivered to us in A PSD layered format.

Here are a couple of example website designs that exemplify what I am after:
1) http://www.plvm.com.au/
2) http://www.thomasvellearchitect.com/en/
3) http://quormel.com/

I particularly like numbers 1 and 2. The third, Quormel, jumps around a little between pages as it is actually several companies. I prefer the page design to remain steady if possible.

I like the very clever nature of number 1 (PLVM). It captures the interest, although slightly gimmicky, however I think it doesn't overpower. Its modern, and visual.

I like the clean elegant design of number 2 (Velle), it simply delivers everything necessary in a clear intelligent manner, its attractive, menu is clever simple to use and attractive.

I would be very happy to have either of these websites.

here is another one:
4) http://www.wnarchitect.com.au/

Although this is similarly elegant, it appears quite dated. I don't like the thumbnails that you click on in the gallery, its quite clumsy. It looks minimalist, and IS minimalist, doesn't look like there is much option to expand other than changing the pictures.

If you look at my own website:
http://www.vantorloom.com.au

I designed and built it myself without any skills or experience. I had to use a generic photo album generator which was worse than useless, the point I am trying to make is I tried to make the menu system a little unusual, I tried to keep the pages neat and tidy, and totally used the "black website" method. However I am more inclined to go with the lighter/white pages of (1) and (2) above because they tend to show photos better.
Updates

Dear Designers. 

ArtBazaarHub Administration has worked to provide a more comprehensive brief. Please review the amended description. 

Kind Regards, Gordon. 

Target Market(s)

Target market is people who are looking to renovate their home

Industry/Entity Type

Construction

Requirements
Must have
• The brief is to design a visual modern, elegant, sophisticated website for a small scale designer/photographer/architect that looks itself like it is designed. Not off the shelf, simple and dated. Basically the design itself has to exemplify me, it has to say "this guy is a designer, and he is good at it".

```html
<!DOCTYPE html>
<html lang="en">
<head>
<meta charset="utf-8">
<title>Vantor Loom – Building Design &amp; Drafting</title>
<link rel="stylesheet" href="https://fonts.googleapis.com/css2?family=Source+Sans+3:wght@400;600;700&display=swap">
<style>
  :root {
    --orange: #e68a00;
    --orange-deep: #d07a00;
    --black: #000000;
    --nav-band: rgba(10, 8, 6, 0.72);
    --white: #ffffff;
    --photo-dark: #2a1d16;
    --photo-warm: #6b3a26;
    --photo-wood: #7a3a22;
    --photo-light: #c9b9a4;
    --circle-dark: #121110;
  }
  * { margin: 0; padding: 0; box-sizing: border-box; }
  html, body {
    width: 1200px; height: 687px; overflow: hidden;
    background: var(--black);
    font-family: "Source Sans 3", "Myriad Pro", Arial, sans-serif;
    color: var(--white);
  }
  .site { position: relative; width: 1200px; height: 687px; }

  .hero {
    position: absolute; left: 0; top: 0; width: 1200px; height: 543px;
    overflow: hidden;
  }
  .hero-photo {
    position: absolute; inset: 0;
    background:
      radial-gradient(ellipse 40% 35% at 78% 85%, rgba(122,58,34,0.9), transparent 70%),
      radial-gradient(ellipse 30% 40% at 92% 60%, rgba(220,210,195,0.75), transparent 70%),
      radial-gradient(ellipse 35% 30% at 20% 30%, rgba(140,60,40,0.8), transparent 70%),
      linear-gradient(180deg, #3a2a22 0%, var(--photo-warm) 35%, #4a3326 60%, var(--photo-dark) 100%);
  }

  .main-nav {
    position: absolute; left: 0; top: 24px; width: 1200px; height: 55px;
    background: var(--nav-band);
  }
  .main-nav a {
    position: absolute; top: 0; line-height: 55px;
    font-size: 13px; font-weight: 400; letter-spacing: 0.2px;
    color: var(--white); text-decoration: none; text-transform: uppercase;
  }
  .main-nav .is-active { color: var(--orange); }
  .nav-home { left: 250px; }
  .nav-about { left: 358px; }
  .nav-services { left: 731px; }
  .nav-contact { left: 874px; }
  .brand {
    position: absolute; left: 540px; top: 0; height: 55px;
    display: flex; align-items: center; gap: 8px;
    font-size: 13px; font-weight: 600; letter-spacing: 2px;
    text-transform: uppercase; color: #d9d9d9;
  }
  .brand-square { width: 10px; height: 10px; background: #d9d9d9; }

  .hero-copy { position: absolute; left: 245px; top: 185px; }
  .hero-title { font-size: 44px; font-weight: 700; line-height: 1; letter-spacing: -0.5px; }
  .hero-sub { font-size: 20px; font-weight: 400; margin-top: 2px; }
  .hero-button {
    display: inline-block; margin-top: 22px;
    background: #111; color: var(--orange);
    font-size: 11.5px; font-weight: 600;
    padding: 6px 10px; border-radius: 2px; text-decoration: none;
  }

  .feature-circle {
    position: absolute; top: 280px; width: 136px; height: 136px; border-radius: 50%;
    display: flex; align-items: center; justify-content: center;
    font-size: 13px; text-transform: uppercase; color: var(--white); text-decoration: none;
  }
  .circle-services { left: 648px; background: var(--orange-deep); }
  .circle-contact { left: 813px; background: var(--circle-dark); }

  .site-footer {
    position: absolute; left: 0; top: 543px; width: 1200px; height: 144px;
    background: var(--black);
  }
  .contact-item { position: absolute; top: 40px; display: flex; align-items: center; gap: 12px; }
  .item-call { left: 248px; }
  .item-mail { left: 530px; }
  .item-follow { left: 817px; }
  .contact-icon {
    width: 40px; height: 40px; border-radius: 50%; background: var(--orange);
    display: flex; align-items: center; justify-content: center;
  }
  .item-follow .contact-icon { background: none; border: 2px solid var(--orange); }
  .contact-label { font-size: 12px; font-weight: 700; line-height: 1.3; }
  .contact-value { font-size: 12px; line-height: 1.3; }
  .social-list { display: flex; gap: 6px; margin-top: 3px; }
  .social-dot { width: 9px; height: 9px; border-radius: 50%; background: var(--white); }
  .footer-rule {
    position: absolute; left: 250px; right: 250px; top: 122px; height: 1px; background: #1a1a1a;
  }
</style>
</head>
<body>
<div class="site">
  <header class="hero">
    <div class="hero-photo" role="img" aria-label="Photograph of a modern kitchen with dark timber cabinets, stone benchtops, a gas cooktop, red appliances and a polished timber floor"></div>

    <nav class="main-nav">
      <a class="nav-home is-active" href="#">Home</a>
      <a class="nav-about" href="#">About us</a>
      <div class="brand"><span class="brand-square"></span>Vantor Loom</div>
      <a class="nav-services" href="#">Services</a>
      <a class="nav-contact" href="#">Contact</a>
    </nav>

    <div class="hero-copy">
      <h1 class="hero-title">Lorem ipsum</h1>
      <p class="hero-sub">dolor sit amet, consectetuer adipiscing elit</p>
      <a class="hero-button" href="#">Find out more &gt;</a>
    </div>

    <a class="feature-circle circle-services" href="#">Our services</a>
    <a class="feature-circle circle-contact" href="#">Our contact</a>
  </header>

  <footer class="site-footer">
    <div class="contact-item item-call">
      <span class="contact-icon">
        <svg width="16" height="22" viewBox="0 0 16 22" aria-hidden="true">
          <rect x="2" y="1" width="12" height="20" rx="2" fill="none" stroke="#fff" stroke-width="2"/>
          <rect x="5" y="4" width="6" height="8" fill="#fff"/>
          <circle cx="8" cy="17" r="1.5" fill="#fff"/>
        </svg>
      </span>
      <div>
        <div class="contact-label">Call</div>
        <div class="contact-value"><b>T :</b> 123 456 789</div>
      </div>
    </div>

    <div class="contact-item item-mail">
      <span class="contact-icon">
        <svg width="20" height="14" viewBox="0 0 20 14" aria-hidden="true">
          <rect x="1" y="1" width="18" height="12" fill="none" stroke="#fff" stroke-width="2"/>
          <path d="M1 1 L10 8 L19 1" fill="none" stroke="#fff" stroke-width="2"/>
        </svg>
      </span>
      <div>
        <div class="contact-label">Contact</div>
        <div class="contact-value">info@mysite.com</div>
      </div>
    </div>

    <div class="contact-item item-follow">
      <span class="contact-icon">
        <svg width="24" height="24" viewBox="0 0 24 24" aria-hidden="true">
          <circle cx="12" cy="12" r="11" fill="var(--orange)"/>
          <path d="M12 6 V18 M6 12 H18" stroke="#fff" stroke-width="3"/>
        </svg>
      </span>
      <div>
        <div class="contact-label">Follow</div>
        <div class="social-list">
          <span class="social-dot"></span><span class="social-dot"></span>
          <span class="social-dot"></span><span class="social-dot"></span>
        </div>
      </div>
    </div>

    <div class="footer-rule"></div>
  </footer>
</div>
</body>
</html>
```